Looking for Desginers for an abstract art canvas & poster stallcraft shop

I want to get a design done for an abstract canvas art & print shop. If possible im looking to create the design based on the harbor or quarry template (im open to suggestions). Mostly I need the creative assets such as banners, images, copywriting, typography etc since im having a hard time to give it a descent look myself.

Target Market(s)

Home decor lovers, abstract art enthusiasts and canvas art enthusiast

Industry/Entity Type

Art

Coding

Coded - Design and coding required

Number of Pages Required

1 page

Colors

Designer to choose only greyscale colors for use in the design.

Requirements
Must have
• Creatives Assets such as banners, images, copy, collection image templates. Please use the velunor logo provided below in at least one of the proposals.
Should not have
• anything that has to be coded into html or css.

```html
<!DOCTYPE html>
<html lang="en">
<head>
<meta charset="utf-8">
<title>Velunor — Abstract Canvas Art &amp; Print</title>
<link href="https://fonts.googleapis.com/css2?family=Inter:wght@400;500;600;700&family=Roboto:wght@500;700&display=swap" rel="stylesheet">
<style>
:root{
  --accent:#d6d6d6;
  --ink:#1f1f1f;
  --body:#4a4a4a;
  --muted:#7a7a7a;
  --line:#cfcfcf;
  --soft:#f4f4f4;
  --dark:#2a2a2a;
  --star:#3a3a3a;
  --white:#ffffff;
  --ph-a:#9c9c9c;
  --ph-b:#6e6e6e;
  --ph-c:#c9c9c9;
}
*{margin:0;padding:0;box-sizing:border-box}
html,body{width:1200px;height:4508px;overflow:hidden}
body{position:relative;background:var(--white);font-family:'Inter',sans-serif;color:var(--body)}
.abs{position:absolute}
.media{position:absolute;display:block}
h2.section-title{position:absolute;font-family:'Roboto',sans-serif;font-weight:500;font-size:28px;color:var(--ink)}
p.copy{position:absolute;font-size:12.5px;line-height:28px;color:var(--body)}
.btn{position:absolute;display:flex;align-items:center;justify-content:center;font-family:'Roboto',sans-serif;font-weight:700;font-size:14px;letter-spacing:.3px;color:var(--ink);background:var(--white);box-shadow:0 4px 10px rgba(0,0,0,.18)}

/* top bar */
.topbar{left:0;top:0;width:1200px;height:38px;background:var(--accent)}
.topbar .note{left:131px;top:11px;font-size:12px;color:var(--ink)}
.topbar .socials{right:136px;top:13px;display:flex;gap:8px}
.topbar .socials span{width:12px;height:12px;border-radius:50%;background:var(--ink);display:block}

/* header */
.header{left:0;top:38px;width:1200px;height:81px;background:var(--white)}
.brand{left:84px;top:20px;font-weight:600;font-size:30px;color:var(--ink);letter-spacing:1px}
.nav{left:432px;top:33px;display:flex;gap:20px;font-family:'Roboto',sans-serif;font-weight:500;font-size:13px;color:var(--ink)}
.tools{left:996px;top:33px;display:flex;gap:10px}

/* hero */
.hero-photo{left:0;top:119px;width:600px;height:600px;background:linear-gradient(180deg,#a3a3a3 0%,#b3b3b3 55%,#d8d8d8 100%)}
.hero-panel{left:600px;top:119px;width:600px;height:600px;background:var(--accent)}
.hero-name{left:600px;top:290px;width:620px;text-align:center;font-weight:600;font-size:64px;color:var(--ink);letter-spacing:2px}
.hero-copy{left:670px;top:406px;width:480px;text-align:center}

/* featured */
.card{position:absolute;top:906px;width:228px;height:308px;border:1px solid var(--line);background:var(--white)}
.card .thumb{position:absolute;left:0;top:0;width:226px;height:226px}
.card .name{position:absolute;left:0;top:248px;width:100%;text-align:center;font-weight:600;font-size:12.5px;color:var(--ink)}
.card .stars{position:absolute;left:0;top:272px;width:100%;text-align:center;font-size:12px;letter-spacing:3px;color:var(--star)}

/* about */
.about-panel{left:0;top:1294px;width:600px;height:464px;background:var(--accent)}
.about-photo{left:600px;top:1294px;width:600px;height:464px;background:linear-gradient(120deg,#5e5e5e 0%,#747474 35%,#8c8c8c 60%,#dcdcdc 100%)}

/* newsletter band */
.band-photo{left:0;top:2917px;width:1200px;height:417px;background:linear-gradient(110deg,#5b5b5b 0%,#7d7d7d 30%,#8d8d8d 55%,#c7c7c7 80%,#e0e0e0 100%)}
.band-box{left:184px;top:2998px;width:832px;height:255px;background:rgba(255,255,255,.55)}
.band-title{left:184px;top:3052px;width:832px;text-align:center;font-family:'Roboto',sans-serif;font-weight:500;font-size:22px;color:var(--ink)}
.band-copy{left:184px;top:3095px;width:832px;text-align:center;font-size:11.5px;color:var(--ink)}
.field{position:absolute;border:1px solid #555;background:transparent;font-size:11.5px;color:var(--ink);display:flex;align-items:center;padding-left:12px}
.submit{position:absolute;background:var(--ink);color:var(--white);font-family:'Roboto',sans-serif;font-weight:700;font-size:14px;display:flex;align-items:center;justify-content:center}

/* news */
.news-title{position:absolute;top:3824px;font-family:'Roboto',sans-serif;font-weight:700;font-size:15px;color:var(--ink);letter-spacing:.2px}

/* footer */
.footer{left:0;top:4010px;width:1200px;height:403px;background:var(--soft)}
.footer-title{left:107px;top:4080px;font-family:'Roboto',sans-serif;font-weight:500;font-size:22px;color:var(--ink)}
.footer-copy{left:107px;top:4116px;width:460px;font-size:11.5px;line-height:28px}
.divider{left:54px;top:4191px;width:1092px;height:1px;background:#777}
.footer-brand{left:120px;top:4250px;font-weight:600;font-size:28px;color:var(--ink);letter-spacing:1px}
.follow{left:147px;top:4330px;font-family:'Roboto',sans-serif;font-weight:700;font-size:14px;color:var(--ink)}
.follow-icons{left:131px;top:4366px;display:flex;gap:16px}
.follow-icons span{width:18px;height:18px;border-radius:4px;background:var(--ink);display:block}
.col{position:absolute;top:4218px}
.col h4{font-family:'Roboto',sans-serif;font-weight:700;font-size:14px;color:var(--ink);margin-bottom:14px}
.col li{list-style:none;font-size:12.5px;line-height:28px;color:var(--body)}

.bottom{left:0;top:4413px;width:1200px;height:95px;background:var(--dark)}
.bottom p{position:absolute;left:0;top:44px;width:1200px;text-align:center;font-size:12px;color:#e5e5e5}
</style>
</head>
<body>

<div class="abs topbar">
  <div class="abs note">Lorem ipsum dolor sit amet, consectetur adipiscing elit, sed do</div>
  <div class="abs socials"><span></span><span></span><span></span><span></span></div>
</div>

<header class="abs header">
  <div class="abs brand">Velunor</div>
  <nav class="abs nav"><span>HOME</span><span>ABOUT</span><span>SHOP</span><span>GALLERY</span><span>CONTACT US</span></nav>
  <div class="abs tools">
    <svg width="14" height="14" viewBox="0 0 14 14"><circle cx="6" cy="6" r="4.2" fill="none" stroke="#1f1f1f" stroke-width="2"/><line x1="9" y1="9" x2="13" y2="13" stroke="#1f1f1f" stroke-width="2.2"/></svg>
    <svg width="14" height="14" viewBox="0 0 14 14"><circle cx="7" cy="4" r="3.2" fill="#1f1f1f"/><path d="M1 14c0-4 3-6 6-6s6 2 6 6z" fill="#1f1f1f"/></svg>
    <svg width="16" height="14" viewBox="0 0 16 14"><path d="M1 5h14l-2 8H3z" fill="#1f1f1f"/><path d="M4 5l3-4M12 5L9 1" stroke="#1f1f1f" stroke-width="1.6" fill="none"/></svg>
  </div>
</header>

<div class="media hero-photo" role="img" aria-label="Living room with a sofa and a wall of abstract canvas prints"></div>
<section class="abs hero-panel"></section>
<div class="abs hero-name">Velunor</div>
<p class="copy hero-copy">Lorem ipsum dolor sit amet, consectetur adipiscing elit, sed do eiusmod tempor incididunt ut labore et dolore magna aliqua. Quis ipsum sus-pendisse ultrices gravida.</p>
<div class="btn" style="left:815px;top:516px;width:191px;height:47px">SHOP NOW</div>

<h2 class="section-title" style="left:131px;top:792px">Our Featured Arts</h2>
<p class="copy" style="left:131px;top:834px;width:730px">Lorem ipsum dolor sit amet, consectetur adipiscing elit, sed do eiusmod tempor incididunt ut labore et dolore magna aliqua. Quis ipsum suspendisse ultrices gravida Risus commodo viverra.</p>

<div class="card" style="left:126px">
  <div class="media thumb" role="img" aria-label="Painted pet portrait canvas" style="background:linear-gradient(135deg,#e6e6e6,#8a8a8a 50%,#5a5a5a)"></div>
  <div class="name">Lorem ipsum dolor sit</div><div class="stars">★★★★★</div>
</div>
<div class="card" style="left:366px">
  <div class="media thumb" role="img" aria-label="Abstract palette-knife painting" style="background:linear-gradient(135deg,#d0d0d0,#7c7c7c 50%,#a6a6a6)"></div>
  <div class="name">Lorem ipsum dolor sit</div><div class="stars">★★★★★</div>
</div>
<div class="card" style="left:605px">
  <div class="media thumb" role="img" aria-label="Abstract palette-knife painting" style="background:linear-gradient(135deg,#e2e2e2,#9a9a9a 55%,#686868)"></div>
  <div class="name">Lorem ipsum dolor sit</div><div class="stars">★★★★★</div>
</div>
<div class="card" style="left:846px">
  <div class="media thumb" role="img" aria-label="Swirling abstract artwork on a dark ground" style="background:linear-gradient(135deg,#1a1a1a,#6a6a6a 45%,#9e9e9e 70%,#141414)"></div>
  <div class="name">Lorem ipsum dolor sit</div><div class="stars">★★★★★</div>
</div>

<section class="abs about-panel"></section>
<div class="media about-photo" role="img" aria-label="Two print technicians inspecting a sheet beside a printing press"></div>
<h2 class="section-title" style="left:75px;top:1376px">About Velunor</h2>
<p class="copy" style="left:75px;top:1424px;width:440px">Lorem ipsum dolor sit amet, consectetur adipiscing elit, sed do ei-usmod tempor incididunt ut labore et dolore magna aliqua. Ut enim ad minim veniam, quis nostrud exercitation ullamco laboris nisi ut aliquip ex ea commodo consequat. Duis aute irure dolor in repre-henderit in voluptate velit esse cillum dolore eu fugiat nulla paria-tur. Excepteur sint occaecat cupidatat non proident.</p>
<div class="btn" style="left:75px;top:1621px;width:189px;height:48px">LEARN MORE</div>

<h2 class="section-title" style="left:131px;top:1833px">Our Gallery</h2>
<p class="copy" style="left:131px;top:1875px;width:730px">Lorem ipsum dolor sit amet, consectetur adipiscing elit, sed do eiusmod tempor incididunt ut labore et dolore magna aliqua. Quis ipsum suspendisse ultrices gravida Risus commodo viverra.</p>
<div class="media" role="img" aria-label="Expressive night-sky landscape painting" style="left:133px;top:1954px;width:390px;height:339px;background:linear-gradient(160deg,#5a5a5a,#7a7a7a 45%,#2e2e2e 85%)"></div>
<div class="media" role="img" aria-label="Wide-format printer head in motion" style="left:533px;top:1954px;width:536px;height:339px;background:linear-gradient(170deg,#e4e4e4,#8c8c8c 35%,#545454 65%,#bcbcbc)"></div>
<div class="media" role="img" aria-label="Close-up palette-knife abstract painting" style="left:133px;top:2302px;width:537px;height:535px;background:linear-gradient(150deg,#b4b4b4 0%,#6c6c6c 45%,#d4d4d4 100%)"></div>
<div class="media" role="img" aria-label="Worker operating a large format printer in a print shop" style="left:679px;top:2302px;width:390px;height:262px;background:linear-gradient(160deg,#d8d8d8,#9d9d9d 50%,#3e3e3e)"></div>
<div class="media" role="img" aria-label="Bright print production hall with machines" style="left:679px;top:2573px;width:390px;height:264px;background:linear-gradient(180deg,#e9e9e9,#bdbdbd 55%,#8f8f8f)"></div>

<div class="media band-photo" role="img" aria-label="Canvas prints leaning against a wall beside a step ladder"></div>
<div class="abs band-box"></div>
<div class="abs band-title">Lorem ipsum dolor sit amet consectetur adipiscing elit.</div>
<div class="abs band-copy">Lorem ipsum dolor sit amet, consectetur adipiscing elit, sed do eiusmod tempor incididunt ut labore et dolore magna aliqua.</div>
<div class="field" style="left:282px;top:3141px;width:467px;height:53px">Enter The Email</div>
<div class="submit" style="left:749px;top:3141px;width:169px;height:53px">SUBSCRIBE</div>

<h2 class="section-title" style="left:0;top:3407px;width:1200px;text-align:center">Our Latest News</h2>
<p class="copy" style="left:240px;top:3449px;width:720px;text-align:center">Lorem ipsum dolor sit amet, consectetur adipiscing elit, sed do eiusmod tempor incididunt ut labore et dolore magna aliqua. Quis ipsum suspendisse ultrices gravida Risus commodo viverra.</p>
<div class="media" role="img" aria-label="Print worker checking a sheet at a workbench" style="left:140px;top:3528px;width:453px;height:278px;background:linear-gradient(150deg,#8a8a8a,#d4d4d4 45%,#555555)"></div>
<div class="media" role="img" aria-label="Two colleagues reviewing prints beside a press" style="left:607px;top:3528px;width:453px;height:278px;background:linear-gradient(150deg,#3c3c3c,#949494 45%,#8c8c8c)"></div>
<div class="news-title" style="left:147px">LOREM IPSUM DOLOR SIT AMET, CONSECTETUR</div>
<div class="news-title" style="left:614px">LOREM IPSUM DOLOR SIT AMET, CONSECTETUR</div>
<p class="copy" style="left:147px;top:3851px;width:430px">Lorem ipsum dolor sit amet, consectetur adipiscing elit, sed do eius-mod tempor incididunt ut labore et dolore magna aliqua. Ut enim ad minim veniam, quis nostrud exercitation ullamco.</p>
<p class="copy" style="left:614px;top:3851px;width:430px">Lorem ipsum dolor sit amet, consectetur adipiscing elit, sed do eius-mod tempor incididunt ut labore et dolore magna aliqua. Ut enim ad minim veniam, quis nostrud exercitation ullamco.</p>

<footer class="abs footer"></footer>
<div class="abs footer-title">Lorem ipsum dolor sit amet consect</div>
<p class="copy footer-copy">Lorem ipsum dolor sit amet, consectetur adipiscing elit, sed do eiusmod tempor incididunt ut labore et dolore magna aliqua.</p>
<div class="field" style="left:575px;top:4098px;width:347px;height:51px">Enter The Email</div>
<div class="submit" style="left:922px;top:4098px;width:171px;height:51px">SUBSCRIBE</div>
<div class="abs divider"></div>
<div class="abs footer-brand">Velunor</div>
<div class="abs follow">FOLLOW US</div>
<div class="abs follow-icons"><span></span><span></span><span></span><span></span></div>
<div class="col" style="left:397px"><h4>QUICK LINKS</h4><ul><li>Home</li><li>About</li><li>Shop</li><li>Gallery</li><li>Contact Us</li></ul></div>
<div class="col" style="left:568px"><h4>IMPORTANT</h4><ul><li>Sitmap</li><li>Privacy Policy</li><li>Terms &amp; Condition</li></ul></div>
<div class="col" style="left:754px"><h4>PRODUCTS</h4><ul><li>Lorem ipsum dolor</li><li>Sit amet, consectetur</li><li>Adipiscing elit</li><li>Sed do eiusmod</li></ul></div>
<div class="col" style="left:960px"><h4>INFORMATION</h4><ul><li>About Us</li><li>Contact Us</li></ul></div>

<div class="abs bottom"><p>© Copyright 2021 &nbsp;Velunor &nbsp;&nbsp;| &nbsp;&nbsp;All Rights Reserved</p></div>

</body>
</html>
```